Etiketten-Design für Weinflasche
Sehr gute Zusammenarbeit bei Tag und Nacht, sehr kooperativ ,flexibel und entgegenkommend. Empfehlenswert
Zielgruppe
Weinbau - Eigenbau Wein -Weinverkauf
Aufgabenstellung
Bräuchte oder Suche ein Flaschenetikette für Rotwein der Marke Zweigelt Das Ausmaß der Etikette sollte 8cm Breit und 12cm Hoch sein. Habe meine letzte Etikette beigelegt sie Anhang

```html
<!DOCTYPE html>
<html lang="de">
<head>
<meta charset="utf-8">
<title>Zweigelt 2020 – Etikett</title>
<link rel="stylesheet" href="https://fonts.googleapis.com/css2?family=Sacramento&family=Source+Serif+4:wght@400&display=swap">
<style>
  :root {
    --paper: #ffffff;
    --label: #202022;
    --glow: #19191b;
    --mark: #38383a;
    --wine: #a50f2d;
    --crop: #222222;
  }
  html, body {
    margin: 0;
    padding: 0;
    width: 1200px;
    height: 1200px;
    overflow: hidden;
    background: var(--paper);
  }
  .canvas {
    position: relative;
    width: 1200px;
    height: 1200px;
  }
  .crop {
    position: absolute;
    background: var(--crop);
  }
  .crop--v { width: 1px; height: 80px; }
  .crop--h { width: 80px; height: 1px; }

  .label {
    position: absolute;
    left: 267px;
    top: 100px;
    width: 666px;
    height: 1000px;
    background: var(--label);
    overflow: hidden;
  }
  .halo {
    position: absolute;
    width: 330px;
    height: 330px;
    border-radius: 50%;
    background: radial-gradient(circle, var(--glow) 35%, rgba(25,25,27,0.6) 60%, rgba(32,32,34,0) 72%);
  }
  .halo--top { left: 179px; top: 57px; }
  .halo--bottom { left: 161px; top: 593px; }

  .house-name {
    position: absolute;
    left: 0;
    width: 100%;
    top: 180px;
    margin: 0;
    text-align: center;
    font-family: "Source Serif 4", serif;
    font-size: 40px;
    color: var(--mark);
    letter-spacing: 2px;
  }
  .variety {
    position: absolute;
    left: 0;
    width: 100%;
    top: 312px;
    margin: 0;
    text-align: center;
    white-space: nowrap;
    font-family: "Sacramento", cursive;
    font-weight: 400;
    font-size: 185px;
    line-height: 1;
    color: var(--wine);
  }
  .vintage {
    position: absolute;
    left: 0;
    width: 100%;
    top: 528px;
    margin: 0;
    text-align: center;
    font-family: "Source Serif 4", serif;
    font-size: 56px;
    letter-spacing: 2px;
    color: var(--wine);
  }
  .region-map {
    position: absolute;
    left: 287px;
    top: 674px;
    width: 90px;
    height: 166px;
    border-radius: 30px 30px 24px 24px;
    background: linear-gradient(180deg, #38383a, #333335);
  }
  .producer {
    position: absolute;
    left: 0;
    width: 100%;
    top: 926px;
    margin: 0;
    text-align: center;
    white-space: nowrap;
    font-family: "Source Serif 4", serif;
    font-size: 33px;
    color: var(--wine);
  }
</style>
</head>
<body>
<div class="canvas">
  <span class="crop crop--v" style="left:267px; top:3px;"></span>
  <span class="crop crop--v" style="left:933px; top:3px;"></span>
  <span class="crop crop--v" style="left:267px; top:1117px;"></span>
  <span class="crop crop--v" style="left:933px; top:1117px;"></span>
  <span class="crop crop--h" style="left:170px; top:100px;"></span>
  <span class="crop crop--h" style="left:950px; top:100px;"></span>
  <span class="crop crop--h" style="left:170px; top:1100px;"></span>
  <span class="crop crop--h" style="left:950px; top:1100px;"></span>

  <section class="label">
    <div class="halo halo--top"></div>
    <div class="halo halo--bottom"></div>
    <p class="house-name">Hainer</p>
    <h1 class="variety">Zweigelt</h1>
    <p class="vintage">2020</p>
    <div class="region-map" role="img" aria-label="Umriss der Weinbauregion"></div>
    <p class="producer">Weinbau Lukas Hainer</p>
  </section>
</div>
</body>
</html>
```